Bright Watt Partners
Simple
Carl Deming
President & CEO
31847 Tillery Lane
Brookeville, MD 20871
carld@brightwattpartners.com
www.brightwattpartners.com
Looking forward to seeing the results. Thanks, Carl
Here is the EPS file. Thanks

```html
<!DOCTYPE html>
<html lang="en">
<head>
<meta charset="utf-8">
<title>Bright Watt Partners — Stationery Set</title>
<link rel="stylesheet" href="https://fonts.googleapis.com/css2?family=Open+Sans:wght@400;600;700&display=swap">
<style>
  :root {
    --stage: #e3e3e3;
    --paper: #ffffff;
    --envelope-back: #9a9a9a;
    --envelope-flap: #b4b4b4;
    --card-back: #a3a3a3;
    --brand-blue: #1f5fae;
    --brand-navy: #1b3a86;
    --brand-green: #5aa51f;
    --brand-lime: #9ccd3c;
    --ink: #3a3a3a;
    --ghost: #c9c9c9;
  }
  * { margin: 0; padding: 0; box-sizing: border-box; }
  html, body { width: 1200px; height: 658px; overflow: hidden; background: var(--stage); font-family: "Open Sans", Arial, sans-serif; color: var(--ink); }
  .stage { position: relative; width: 1200px; height: 658px; }
  .sheet { position: absolute; background: var(--paper); box-shadow: 0 2px 6px rgba(0,0,0,.25); overflow: hidden; }
  address { font-style: normal; }

  .brand-name { font-family: "Open Sans", Arial, sans-serif; font-weight: 700; color: var(--brand-blue); white-space: nowrap; display: flex; align-items: center; gap: 6px; }
  .brand-mark { display: inline-block; border-radius: 50%; background: var(--brand-green); }

  .wave-band {
    position: absolute; left: 0; bottom: 0; width: 100%;
    background: linear-gradient(to bottom, rgba(255,255,255,0) 0%, rgba(255,255,255,0) 8%, transparent 8%),
                linear-gradient(100deg, #4aa21f 0%, #7cbf3a 45%, #3a7cc8 75%, #1b3a86 100%);
    opacity: .9;
  }

  /* Letterhead */
  .letterhead { left: 233px; top: 29px; width: 396px; height: 621px; }
  .letterhead .brand-name { position: absolute; left: 26px; top: 24px; font-size: 16px; }
  .letterhead .brand-mark { width: 9px; height: 9px; }
  .letterhead .rule-lines { position: absolute; left: 228px; right: 0; top: 34px; }
  .rule-lines span { display: block; height: 2px; margin-bottom: 3px; }
  .rule-lines .green { background: var(--brand-green); }
  .rule-lines .blue { background: var(--brand-blue); }
  .letterhead .wave-band { height: 110px; }
  .letterhead .contact { position: absolute; left: 55px; bottom: 10px; font-size: 5px; line-height: 1.45; color: var(--paper); }

  /* Envelopes */
  .envelope-back { left: 696px; top: 98px; width: 485px; height: 226px; background: var(--envelope-back); }
  .envelope-back .flap { position: absolute; inset: 0; width: 100%; height: 100%; }
  .envelope-back .brand-name { position: absolute; left: 50%; top: 88px; transform: translateX(-50%); font-size: 26px; color: var(--ghost); }

  .envelope-front { left: 696px; top: 346px; width: 485px; height: 273px; }
  .envelope-front .brand-name { position: absolute; left: 18px; top: 22px; font-size: 18px; }
  .envelope-front .brand-mark { width: 10px; height: 10px; }
  .envelope-front .wave-band { height: 70px; }
  .envelope-front .contact { position: absolute; left: 20px; top: 100px; font-size: 8px; line-height: 1.45; }
  .contact strong { font-weight: 600; }

  /* Business cards */
  .card-back { left: 19px; top: 336px; width: 187px; height: 108px; background: var(--card-back); display: flex; align-items: center; justify-content: center; }
  .card-back .brand-name { font-size: 14px; color: var(--ghost); }

  .card-front { left: 19px; top: 468px; width: 187px; height: 115px; }
  .card-front .brand-name { position: absolute; left: 8px; top: 13px; font-size: 9px; }
  .card-front .brand-mark { width: 6px; height: 6px; }
  .card-front .person { position: absolute; right: 10px; top: 12px; text-align: left; }
  .person .name { font-size: 8px; font-weight: 600; color: var(--brand-navy); }
  .person .title { font-size: 5px; }
  .card-front .wave-band { height: 30px; }
  .card-front .contact { position: absolute; left: 8px; top: 40px; font-size: 4.5px; line-height: 1.4; }
</style>
</head>
<body>
<main class="stage">
  <section class="sheet letterhead">
    <div class="brand-name"><span class="brand-mark"></span>Bright Watt Partners</div>
    <div class="rule-lines"><span class="green"></span><span class="blue"></span></div>
    <div class="wave-band" role="img" aria-label="Green and blue decorative wave band"></div>
    <address class="contact">
      31847 Tillery Lane<br>Brookeville, MD 20871<br>
      carld@brightwattpartners.com<br>www.brightwattpartners.com
    </address>
  </section>

  <section class="sheet envelope-back">
    <svg class="flap" viewBox="0 0 485 226" preserveAspectRatio="none" aria-hidden="true">
      <path d="M0,0 L485,0 L242,130 Z" fill="var(--envelope-flap)"/>
    </svg>
    <div class="brand-name">Bright Watt Partners</div>
  </section>

  <section class="sheet envelope-front">
    <div class="brand-name"><span class="brand-mark"></span>Bright Watt Partners</div>
    <address class="contact">
      <strong>31847 Tillery Lane</strong><br>
      Brookeville, MD 20871<br>
      Cell: 301-555-0142 Phone: 301-555-0187 Fax: 301-555-0163<br>
      Email: carld@brightwattpartners.com<br>
      Web address: www.brightwattpartners.com
    </address>
    <div class="wave-band" role="img" aria-label="Green and blue decorative wave band"></div>
  </section>

  <section class="sheet card-back">
    <div class="brand-name">Bright Watt Partners</div>
  </section>

  <section class="sheet card-front">
    <div class="brand-name"><span class="brand-mark"></span>Bright Watt Partners</div>
    <div class="person">
      <div class="name">Carl Deming</div>
      <div class="title">President &amp; CEO</div>
    </div>
    <address class="contact">
      31847 Tillery Lane<br>Brookeville, MD 20871<br>
      carld@brightwattpartners.com<br>www.brightwattpartners.com
    </address>
    <div class="wave-band" role="img" aria-label="Green and blue decorative wave band"></div>
  </section>
</main>
</body>
</html>
```